Wordpress theme for "plinkovault.net"

I am starting a Sports Blog called "Tallying @ Porch". I need a WordPress theme for the blog. I envisioned a theme with different sports score cards in the background (baseball, football, basketball, bowling, golf, cricket, etc.).
I know what I want, but it is hard to describe. I obviously want a professional looking blog (who doesn't) that is easy to navigate.
I like to have fun and be funny, and while I will post serious subjects, I want people to know I don't take myself too seriously.
Updates
I am afraid I may not have been entirely clear on the project, and I apologize. The blog is going to be about sports and social commentary. As far as the layout is concerned, I would like a three column layout with links to other blogs on one side and archives on the other. Also, I have found PICTURES of different types of scorecards on the internet, and I would like those images to be the BACKGROUND for the site, if possible.

```html
<!DOCTYPE html>
<html lang="en">
<head>
<meta charset="utf-8">
<title>Tallying @ Porch</title>
<link rel="stylesheet" href="https://fonts.googleapis.com/css2?family=Lato:wght@400;700&display=swap">
<style>
:root{
  --blue:#1e88d8;
  --blue-dark:#0f5e9c;
  --ink:#2a2a2a;
  --text:#555;
  --muted:#999;
  --line:#e6e6e6;
  --bar:#232323;
  --bar-2:#333;
  --page:#ededed;
  --card:#fff;
}
*{box-sizing:border-box;margin:0;padding:0}
html,body{width:819px;height:1200px;overflow:hidden}
body{position:relative;font-family:"Lato",Arial,sans-serif;color:var(--text);background:var(--page)}
a{color:inherit;text-decoration:none}
ul{list-style:none}

.page-backdrop{position:absolute;left:0;top:55px;width:819px;height:1046px;
  background:linear-gradient(180deg,#eeeeee,#e4e4e4 50%,#ececec)}

/* header */
.site-header{position:absolute;left:0;top:0;width:819px;height:55px;background:var(--bar);border-top:2px solid var(--blue)}
.brand{position:absolute;left:130px;top:12px;display:flex;align-items:center;gap:8px}
.brand-mark{width:30px;height:30px;background:var(--blue);border-radius:3px}
.brand-name{font-size:27px;font-weight:400;color:#fff;letter-spacing:-.3px}
.search{position:absolute;left:409px;top:17px;display:flex;align-items:center;gap:8px}
.search-label,.follow-label{font-size:7px;font-weight:700;color:#888;letter-spacing:.4px}
.search-field{width:120px;height:18px;background:#3a3a3a;border-radius:2px;position:relative}
.search-field svg{position:absolute;right:6px;top:3px}
.follow{position:absolute;left:583px;top:18px;display:flex;align-items:center;gap:5px}
.follow-label{margin-right:3px}
.dot{width:17px;height:17px;border-radius:50%;background:#777;display:inline-block}

/* nav */
.nav-wrap{position:absolute;left:122px;top:62px;width:575px;height:45px;background:var(--card)}
.main-nav{position:absolute;left:0;top:4px;width:575px;height:28px;background:var(--blue);display:flex;align-items:center;justify-content:center}
.main-nav a{font-size:8px;font-weight:700;color:#fff;padding:0 11px;position:relative}
.main-nav a+a::before{content:"|";position:absolute;left:-2px;color:#fff}

/* columns */
.widget{position:absolute;background:var(--card);box-shadow:0 1px 3px rgba(0,0,0,.12);padding:33px 8px 6px;overflow:hidden}
.ribbon{position:absolute;top:11px;height:22px;background:var(--blue);color:#fff;font-size:8.5px;font-weight:700;display:flex;align-items:center;justify-content:center;letter-spacing:.2px}
.left .ribbon{left:-8px;width:140px;clip-path:polygon(0 0,100% 0,96% 100%,0 100%)}
.right .ribbon{right:-8px;width:140px;clip-path:polygon(0 0,100% 0,100% 100%,4% 100%)}
.links li{font-size:7.5px;color:#444;height:18.5px;line-height:18.5px;border-bottom:1px solid var(--line);padding-left:13px;position:relative}
.links li:last-child{border-bottom:0}
.links li::before{content:"";position:absolute;left:5px;top:8px;width:3px;height:3px;background:var(--blue)}

.feed li{padding:5px 0 6px;border-bottom:1px solid var(--line);position:relative}
.feed li:last-child{border-bottom:0}
.feed .feed-title{display:block;font-size:7px;font-weight:700;color:var(--blue);text-align:center;line-height:11.5px;padding:0 2px 0 12px}
.feed .feed-title::before{content:"";position:absolute;left:3px;top:9px;width:4px;height:4px;border-left:1.2px solid var(--blue);border-top:1.2px solid var(--blue);transform:rotate(45deg)}
.feed p{font-size:7px;line-height:11.5px;text-align:center;color:#666;margin-top:6px}

.tags{font-size:8px;line-height:15px;color:#555;padding:0 4px}
.tags b{color:#333}
.tags .t-lg{font-size:10px;font-weight:700;color:#333}
.tags .t-md{font-size:9px}

.tweet{text-align:center;padding:4px 0 8px;border-bottom:1px solid var(--line)}
.tweet:last-child{border-bottom:0}
.tweet .handle{font-size:7.5px;font-weight:700;color:var(--blue);line-height:10px}
.tweet p{font-size:7px;line-height:11.5px;color:#666;margin:8px 0 7px}
.tweet time{display:block;font-size:6.5px;line-height:8px;color:#aaa}

/* posts */
.featured{position:absolute;left:283px;top:120px;width:253px;height:970px;background:var(--card);box-shadow:0 1px 3px rgba(0,0,0,.12)}
.featured h2{position:absolute;left:11px;top:12px;font-size:8.5px;font-weight:700;color:var(--ink)}
.featured h2 span{color:var(--blue)}
.post{position:absolute;left:11px;width:231px}
.post-media{width:231px;height:132px;background:linear-gradient(180deg,#5a5f5a 0%,#4d6b3a 55%,#3f7a2f 100%);position:relative}
.play{position:absolute;left:98px;top:48px;width:36px;height:36px;border-radius:50%;background:#fff}
.play::after{content:"";position:absolute;left:14px;top:10px;border-style:solid;border-width:8px 0 8px 12px;border-color:transparent transparent transparent var(--blue)}
.post-date{position:absolute;left:-20px;top:142px;width:30px;height:28px;background:var(--blue);color:#fff;text-align:center;clip-path:polygon(25% 0,75% 0,100% 50%,75% 100%,25% 100%,0 50%)}
.post-date b{display:block;font-size:11px;line-height:12px;margin-top:3px}
.post-date small{display:block;font-size:6px;font-weight:700}
.post-title{margin:12px 0 0 15px;font-size:9.5px;font-weight:400;line-height:14px;color:var(--ink)}
.post-body{font-size:7px;line-height:12.2px;color:#666;margin-top:8px}
.post-meta{margin-top:12px;border-top:1px solid var(--line);padding-top:6px;font-size:7px;color:var(--blue);display:grid;grid-template-columns:1fr auto;row-gap:8px}
.meta-item{display:flex;align-items:center;gap:5px}
.ico{width:8px;height:8px;background:var(--blue);display:inline-block}
.ico.heart{clip-path:polygon(50% 100%,0 40%,15% 5%,50% 25%,85% 5%,100% 40%)}
.ico.bubble{width:11px;height:7px;border-radius:50%}
.share{display:flex;align-items:center;gap:2px;justify-content:flex-end}
.share .dot{width:9px;height:9px;background:var(--blue)}
.share span{margin-left:4px}

/* footer */
.footer-nav{position:absolute;left:0;top:1101px;width:819px;height:36px;background:var(--bar-2);display:flex;align-items:center;justify-content:center}
.footer-nav a{font-size:7.5px;color:#aaa;padding:0 12px;position:relative}
.footer-nav a+a::before{content:"|";position:absolute;left:-2px}
.site-footer{position:absolute;left:0;top:1137px;width:819px;height:63px;background:var(--bar)}
.site-footer .social{position:absolute;left:381px;top:14px;display:flex;gap:5px}
.site-footer .social .dot{width:16px;height:16px}
.copyright{position:absolute;left:0;top:45px;width:100%;text-align:center;font-size:7px;color:#888}
</style>
</head>
<body>

<div class="page-backdrop" role="img" aria-label="Faint background collage of sports scorecards and athlete silhouettes"></div>

<header class="site-header">
  <a class="brand" href="#"><span class="brand-mark"></span><span class="brand-name">Tallying@Porch</span></a>
  <div class="search"><span class="search-label">SEARCH</span>
    <span class="search-field"><svg width="12" height="12" viewBox="0 0 12 12"><circle cx="5" cy="5" r="3.6" fill="none" stroke="#999" stroke-width="1.4"/><line x1="7.6" y1="7.6" x2="11" y2="11" stroke="#999" stroke-width="1.6"/></svg></span>
  </div>
  <div class="follow"><span class="follow-label">FOLLOW US</span><span class="dot"></span><span class="dot"></span><span class="dot"></span></div>
</header>

<div class="nav-wrap">
  <nav class="main-nav">
    <a href="#">RIDGE OTTER FOOTBALL</a><a href="#">PGL</a><a href="#">PBL</a><a href="#">COLLEGE FB</a><a href="#">PHL</a><a href="#">RIDGE OTTER BASKETBALL</a><a href="#">TALKING POINTS</a><a href="#">OTTERS</a>
  </nav>
</div>

<aside class="left">
  <section class="widget" style="left:130px;top:120px;width:142px;height:133px">
    <h3 class="ribbon">IMPORTANT LINKS</h3>
    <ul class="links"><li>Home</li><li>Deadpost</li><li>Awkward Announcing</li><li>TVsportswire</li><li>SPRX</li></ul>
  </section>

  <section class="widget" style="left:130px;top:263px;width:142px;height:425px">
    <h3 class="ribbon">RECENT POSTS</h3>
    <ul class="feed">
      <li><a class="feed-title" href="#">Ut lacus enim, blandit ut velit a, dapibus lobortis</a><p>Ut lacus enim, blandit ut velit a, dapibus lobortis purus. Phasellus rhoncus sit amet lacus eu vestibulum.</p></li>
      <li><a class="feed-title" href="#">Ut lacus enim, blandit ut velit a, dapibus lobortis</a></li>
      <li><a class="feed-title" href="#">Ut lacus enim, blandit ut velit a, dapibus lobortis</a></li>
      <li><a class="feed-title" href="#">Ut lacus enim, blandit ut velit a, dapibus lobortis</a></li>
      <li><a class="feed-title" href="#">Ut lacus enim, blandit ut velit a, dapibus lobortis</a></li>
      <li><a class="feed-title" href="#">Ut lacus enim, blandit ut velit a, dapibus lobortis</a></li>
      <li><a class="feed-title" href="#">Ut lacus enim, blandit ut velit a, dapibus lobortis</a></li>
      <li><a class="feed-title" href="#">Ut lacus enim, blandit ut velit a, dapibus lobortis</a></li>
      <li><a class="feed-title" href="#">Ut lacus enim, blandit ut velit a, dapibus lobortis</a></li>
      <li><a class="feed-title" href="#">Ut lacus enim, blandit ut velit a, dapibus lobortis</a></li>
    </ul>
  </section>

  <section class="widget" style="left:130px;top:698px;width:142px;height:226px">
    <h3 class="ribbon">RELATED BLOGS</h3>
    <ul class="links"><li>Home</li><li>Deadpost</li><li>Awkward Announcing</li><li>TVsportswire</li><li>SPRX</li><li>Home</li><li>Deadpost</li><li>Awkward Announcing</li><li>TVsportswire</li><li>SPRX</li></ul>
  </section>
</aside>

<main class="featured">
  <h2>FEATURED <span>ARTICLES</span></h2>

  <article class="post" style="top:40px">
    <div class="post-media" role="img" aria-label="Photo of two footballers contesting the ball on a pitch"></div>
    <div class="post-date"><b>29</b><small>SEP</small></div>
    <h3 class="post-title">Lorem ipsum dolor sit amet, consectetur adipiscing elit, Nullam lorem urna.</h3>
    <p class="post-body">Lorem ipsum dolor sit amet, consectetur adipiscing elit. Nullam lorem urna, malesuada quis faucibus vitae, interdum sodales turpis. Donec vitae scelerisque nibh. Suspendisse eu massa sagittis diam sollicitudin tristique sit amet a orci. Morbi hendrerit lobortis velit in dictum. Cras euismod a est eget consequat. Donec orci massa, volutpat vitae gravida at, dictum in leo.</p>
    <div class="post-meta">
      <span class="meta-item"><i class="ico"></i>September 29, 2013</span>
      <span class="meta-item"><i class="ico bubble"></i>2 Comments</span>
      <span class="meta-item"><i class="ico heart"></i>Leave a Comments</span>
      <span class="share"><i class="dot"></i><i class="dot"></i><i class="dot"></i><span>Share</span></span>
    </div>
  </article>

  <article class="post" style="top:371px">
    <div class="post-media" role="img" aria-label="Photo of two footballers contesting the ball on a pitch"></div>
    <div class="post-date"><b>30</b><small>SEP</small></div>
    <h3 class="post-title">Lorem ipsum dolor sit amet, consectetur adipiscing elit, Nullam lorem urna.</h3>
    <p class="post-body">Lorem ipsum dolor sit amet, consectetur adipiscing elit. Nullam lorem urna, malesuada quis faucibus vitae, interdum sodales turpis. Donec vitae scelerisque nibh. Suspendisse eu massa sagittis diam sollicitudin tristique sit amet a orci.</p>
    <div class="post-meta">
      <span class="meta-item"><i class="ico"></i>September 29, 2013</span>
      <span class="meta-item"><i class="ico bubble"></i>2 Comments</span>
      <span class="meta-item"><i class="ico heart"></i>Leave a Comments</span>
      <span class="share"><i class="dot"></i><i class="dot"></i><i class="dot"></i><span>Share</span></span>
    </div>
  </article>

  <article class="post" style="top:676px">
    <div class="post-media" role="img" aria-label="Video still of two footballers contesting the ball on a pitch"><span class="play"></span></div>
    <div class="post-date"><b>01</b><small>OCT</small></div>
    <h3 class="post-title">Lorem ipsum dolor sit amet, consectetur adipiscing elit, Nullam lorem urna.</h3>
    <p class="post-body">Lorem ipsum dolor sit amet, consectetur adipiscing elit. Nullam lorem urna, malesuada quis faucibus vitae, interdum sodales turpis. Donec vitae scelerisque nibh. Suspendisse eu massa sagittis diam sollicitudin tristique sit amet a orci.</p>
    <div class="post-meta">
      <span class="meta-item"><i class="ico"></i>September 29, 2013</span>
      <span class="meta-item"><i class="ico bubble"></i>2 Comments</span>
      <span class="meta-item"><i class="ico heart"></i>Leave a Comments</span>
      <span class="share"><i class="dot"></i><i class="dot"></i><i class="dot"></i><span>Share</span></span>
    </div>
  </article>
</main>

<aside class="right">
  <section class="widget" style="left:547px;top:120px;width:142px;height:133px">
    <h3 class="ribbon">CATEGORIES</h3>
    <ul class="links"><li>Otters</li><li>College FB</li><li>PBL</li><li>PGL</li><li>Ridge Otter Football</li></ul>
  </section>

  <section class="widget" style="left:547px;top:263px;width:142px;height:253px">
    <h3 class="ribbon">RECENT COMMENTS</h3>
    <ul class="feed">
      <li><a class="feed-title" href="#">Ut lacus enim, blandit ut velit a, dapibus lobortis</a><p>Ut lacus enim, blandit ut velit a, dapibus lobortis purus. Phasellus rhoncus sit amet lacus eu vestibulum.</p></li>
      <li><a class="feed-title" href="#">Ut lacus enim, blandit ut velit a, dapibus lobortis</a></li>
      <li><a class="feed-title" href="#">Ut lacus enim, blandit ut velit a, dapibus lobortis</a></li>
      <li><a class="feed-title" href="#">Ut lacus enim, blandit ut velit a, dapibus lobortis</a></li>
      <li><a class="feed-title" href="#">Ut lacus enim, blandit ut velit a, dapibus lobortis</a></li>
    </ul>
  </section>

  <section class="widget" style="left:547px;top:526px;width:142px;height:142px">
    <h3 class="ribbon">TAGS</h3>
    <p class="tags">Aenean <span class="t-md"><b>nec</b></span> massa <span class="t-md">eget</span> nisi <b>faucibus</b> viverra. <span class="t-lg">Nullam</span> mi elit, scelerisque <span class="t-md"><b>sitamet</b></span> commodo Aenean <span class="t-md"><b>nec</b></span> massa <span class="t-md">eget</span> nisi <b>faucibus</b> viverra. <span class="t-lg">Nullam</span> mi elit, scelerisque <span class="t-md"><b>sitamet</b></span> commodo</p>
  </section>

  <section class="widget" style="left:547px;top:678px;width:142px;height:370px">
    <h3 class="ribbon">LATEST TWEETS</h3>
    <div class="tweet"><div class="handle">@loremipsum</div><p>Ut lacus enim, blandit ut velit a, dapibus lobortis purus. Phasellus rhoncus sit amet lacus eu vestibulum.</p><time>20 Minutes Ago</time></div>
    <div class="tweet"><div class="handle">@loremipsum</div><p>Ut lacus enim, blandit ut velit a, dapibus lobortis purus. Phasellus rhoncus sit amet lacus eu vestibulum.</p><time>20 Minutes Ago</time></div>
    <div class="tweet"><div class="handle">@loremipsum</div><p>Ut lacus enim, blandit ut velit a, dapibus lobortis purus. Phasellus rhoncus sit amet lacus eu vestibulum.</p><time>20 Minutes Ago</time></div>
    <div class="tweet"><div class="handle">@loremipsum</div><p>Ut lacus enim, blandit ut velit a, dapibus lobortis purus. Phasellus rhoncus sit amet lacus eu vestibulum.</p><time>20 Minutes Ago</time></div>
  </section>
</aside>

<nav class="footer-nav">
  <a href="#">Ridge Otter Football</a><a href="#">PGL</a><a href="#">PBL</a><a href="#">College FB</a><a href="#">PHL</a><a href="#">Ridge Otter Basketball</a><a href="#">Talking Points</a><a href="#">Otters</a>
</nav>

<footer class="site-footer">
  <div class="social"><span class="dot"></span><span class="dot"></span><span class="dot"></span></div>
  <p class="copyright">Copyright © Tallying @ Porch 2013 . All Rights Reserved.</p>
</footer>

</body>
</html>
```